We operate a niche online Job Board in Australia. The website is called 'Harvest Roles Australia' and is used by Christian Employers to advertise their job vacancies.
I would like a business card that identifies with our website (www.harvestroles-example.com.au). We would like the same colors and fonts used on our business card from our website. When people look at our business card we want them to be able to recognise it from the website.
We want the web address to be dominant.
Updates
We are liking those that use white space as well as the blue and orange and those that highlight the url.
We now have 60 designs and therefore will not wait for the Sunday deadline to make a decision. We have a few we like.
The ones we like are:
- bold
- creative
- colorful (blue orange and white)
- some white space
- no boxes or borders
- font the same as our website
- reflects the look of our website
We will make a final decision in the next 6 hours so please if you think you have something to offer then get it in within the next 6 hours. If you think you will leave it till later you will miss out. Thanks to all those who have responded with some great designs, sorry we can't reward all of you!
Industry/Entity Type
Business
Contact Information for Business Card
Harvest Roles Australia
www.harvestroles-example.com.au
Peter Galvridge
CEO
Phone: 1300 512 874
Mobile: 0412 735019
Fax: (03) 9157 2360
email: peter@harvestroles-example.com.au
Requirements
Should not have
- We do not want a cross or any cliche christian images.

```html
<!DOCTYPE html>
<html lang="en">
<head>
<meta charset="utf-8">
<title>Harvest Roles Australia – Business Card</title>
<link href="https://fonts.googleapis.com/css2?family=Crimson+Pro:wght@500;700&family=Questrial&display=swap" rel="stylesheet">
<style>
  :root {
    --backdrop: #2b2b2d;
    --navy: #1e1c5c;
    --navy-light: #25237a;
    --navy-deep: #141245;
    --orange: #f6a24a;
    --orange-band-top: #fdb35c;
    --orange-band-bottom: #f5901f;
    --white: #ffffff;
  }
  * { margin: 0; padding: 0; box-sizing: border-box; }
  html, body {
    width: 1200px;
    height: 1000px;
    overflow: hidden;
    background: var(--backdrop);
  }
  .card {
    position: absolute;
    left: 134px;
    top: 253px;
    width: 907px;
    height: 518px;
    background: radial-gradient(ellipse 60% 70% at 30% 45%, var(--navy-light) 0%, var(--navy) 70%);
    overflow: hidden;
    box-shadow: 0 6px 22px rgba(0,0,0,0.45);
  }
  .divider {
    position: absolute;
    left: 420px;
    top: 100px;
    width: 4px;
    height: 330px;
    background: linear-gradient(to bottom, transparent, var(--navy-deep) 30%, var(--navy-deep) 70%, transparent);
    filter: blur(1px);
  }
  .brand-name {
    position: absolute;
    left: 31px;
    top: 228px;
    width: 370px;
    font-family: "Crimson Pro", serif;
    font-weight: 700;
    font-size: 31px;
    line-height: 40px;
    color: var(--white);
    white-space: nowrap;
  }
  .person {
    position: absolute;
    left: 463px;
    top: 204px;
    font-family: "Crimson Pro", serif;
    font-weight: 500;
    font-size: 37px;
    line-height: 44px;
    color: var(--white);
    white-space: nowrap;
  }
  .person-title { color: var(--orange); }
  .contact-list {
    position: absolute;
    left: 497px;
    top: 270px;
    list-style: none;
    font-family: "Questrial", sans-serif;
    font-size: 15.5px;
    line-height: 21.5px;
    color: var(--white);
    text-transform: uppercase;
    white-space: nowrap;
  }
  .contact-label { font-weight: 700; letter-spacing: 0.3px; }
  .accent { color: var(--orange); }
  .web-band {
    position: absolute;
    left: 0;
    bottom: 0;
    width: 100%;
    height: 44px;
    background: linear-gradient(to bottom, var(--orange-band-top), var(--orange-band-bottom));
    text-align: center;
    font-family: "Crimson Pro", serif;
    font-weight: 700;
    font-size: 32px;
    line-height: 42px;
    color: var(--white);
    text-shadow: 0 1px 2px rgba(120,60,0,0.35);
  }
</style>
</head>
<body>
  <div class="card">
    <div class="divider"></div>

    <div class="brand-name">Harvest Roles Australia</div>

    <div class="person">Peter Galvridge <span class="person-title">CEO</span></div>

    <ul class="contact-list">
      <li><span class="contact-label">Phone:</span> 1300 512 874</li>
      <li><span class="contact-label">Mobile:</span> 0412 735019</li>
      <li><span class="contact-label">Fax:</span> (03) 9157 2360</li>
      <li><span class="contact-label">Email:</span> peter@harvest<span class="accent">roles</span>-example.com.au</li>
    </ul>

    <div class="web-band">www.harvestroles-example.com.au</div>
  </div>
</body>
</html>
```